The amber lantern with an elephant incorporated in the background

Target Market(s)

Real estate

Industry/Entity Type

Real Estate

Contact Information for Business Card

On back on want my name & number
In front I want the business name, "the amber lantern", below to say staging & design

Logo Text

The amber lantern

Font styles to use
Serif

Colors
000000

Requirements
Must have
• I want an elephant behind the writing in gold transperant

```html
<!DOCTYPE html>
<html lang="en">
<head>
<meta charset="utf-8">
<title>The Amber Lantern – Business Card</title>
<link rel="stylesheet" href="https://fonts.googleapis.com/css2?family=Cinzel:wght@400&family=Oswald:wght@400&family=Roboto:wght@400&family=Quicksand:wght@400&display=swap">
<style>
  :root {
    --canvas-bg: #e6e3df;
    --card-white: #ffffff;
    --card-black: #0a0a0a;
    --ink: #4a4a4a;
    --ink-soft: #555555;
    --gold: #c9a94a;
    --subtitle: #f2f2f2;
  }
  * { margin: 0; padding: 0; box-sizing: border-box; }
  html, body {
    width: 1200px; height: 1200px; overflow: hidden;
    background: var(--canvas-bg);
  }
  .canvas { position: relative; width: 1200px; height: 1200px; }
  .card {
    position: absolute; left: 214px; width: 772px; height: 440px;
    overflow: hidden;
    box-shadow: 0 6px 18px rgba(0,0,0,0.25);
  }
  .card--contact { top: 150px; background: var(--card-white); }
  .card--brand { top: 634px; background: var(--card-black); }

  .person {
    position: absolute; right: 421px; top: 186px; text-align: right;
  }
  .person__name {
    font-family: "Oswald", "Arial Narrow", sans-serif;
    font-size: 38px; font-weight: 400; color: var(--ink);
    letter-spacing: 0.5px; line-height: 1.1; text-transform: uppercase;
  }
  .person__title {
    font-family: "Roboto", Arial, sans-serif;
    font-size: 19px; color: var(--ink-soft); margin-top: 4px;
  }
  .divider {
    position: absolute; left: 388px; top: 187px; width: 1.5px; height: 72px;
    background: var(--ink);
  }
  .contact-list {
    position: absolute; left: 423px; top: 182px; list-style: none;
    font-family: "Roboto", Arial, sans-serif; font-size: 19px; color: var(--ink-soft);
  }
  .contact-list li { display: flex; align-items: center; height: 27.5px; }
  .contact-list svg { width: 17px; height: 17px; margin-right: 6px; flex: none; }

  .brand-dot {
    position: absolute; left: 341px; top: 100px; width: 90px; height: 90px;
    border-radius: 50%; background: var(--gold);
  }
  .brand-name {
    position: absolute; left: 0; right: 0; top: 255px; text-align: center;
    font-family: "Cinzel", "Times New Roman", serif;
    font-size: 42px; font-weight: 400; color: var(--gold);
    letter-spacing: 1.5px; text-transform: uppercase; line-height: 1.2;
  }
  .brand-tagline {
    position: absolute; left: 0; right: 0; top: 308px; text-align: center;
    font-family: "Quicksand", Arial, sans-serif;
    font-size: 24px; color: var(--subtitle);
  }
</style>
</head>
<body>
<main class="canvas">
  <section class="card card--contact">
    <div class="person">
      <p class="person__name">Marcus Hale</p>
      <p class="person__title">President &amp; CEO</p>
    </div>
    <div class="divider"></div>
    <ul class="contact-list">
      <li>
        <svg viewBox="0 0 24 24" fill="none" stroke="#555" stroke-width="1.6"><path d="M5 3h4l2 5-2.5 1.5a11 11 0 0 0 6 6L16 13l5 2v4a2 2 0 0 1-2 2A16 16 0 0 1 3 5a2 2 0 0 1 2-2z"/></svg>
        000-000-0000
      </li>
      <li>
        <svg viewBox="0 0 24 24" fill="none" stroke="#555" stroke-width="1.6"><rect x="3" y="6" width="18" height="12"/><path d="M3 6l9 7 9-7"/></svg>
        hale@sample-mail.com
      </li>
      <li>
        <svg viewBox="0 0 24 24" fill="none" stroke="#555" stroke-width="1.6"><circle cx="12" cy="12" r="9"/><path d="M3 12h18M12 3c3 3 3 15 0 18M12 3c-3 3-3 15 0 18"/></svg>
        www.sample-mail.com
      </li>
    </ul>
  </section>

  <section class="card card--brand">
    <div class="brand-dot"></div>
    <h1 class="brand-name">The Amber Lantern</h1>
    <p class="brand-tagline">staging &amp; design</p>
  </section>
</main>
</body>
</html>
```